Plenvoria - You are the Boss!

Plenvoria is a new Silicon Valley company, of the kirvel founders from Berlin, which provides a "Open Tandem Weave". This platform allows the crowd to support startups with money, experts and fame. Our Vision is, that everyone should become an entrepreneur.

Pls find all brief details in the attached document
Updates

Would be nice to have a list of more social services I'm available on, like a list of pictograms of all my services:

Find me on: vexlo, ramply+, tqv, brisko, dowmerit, fesk, wumpel, etc...

pls make sure to use the right font:
http://www.lettrovane.com/fonts/Orbitron

Target Market(s)

Main target market is those already involved in the startup industry, by fundraising, investing, advising, cofounding and working. Plenvoria brings a totaly new transparency and collaborative way of starting companies to that business.

· Entrepreneurs (looking for funding, team and community)
· Investors (looking for hot investments and )
· Experts (workers looking for startups they can work for equity)
· Incubators & Business Schools (looking for tools to advise startups)

Industry/Entity Type

It Company

Requirements
Must have
• Pls find all brief details in the attached document
Nice to have

```html
<!DOCTYPE html>
<html lang="en">
<head>
<meta charset="utf-8">
<title>Plenvoria – Business Card</title>
<link rel="stylesheet" href="https://fonts.googleapis.com/css2?family=Orbitron:wght@900&family=Open+Sans:ital,wght@0,400;0,600;1,600&family=Cinzel&display=swap">
<style>
  :root {
    --stage: #e6e6e6;
    --orange: #ef6a3c;
    --card-light: #f1f1f1;
    --card-shade: #dcdcdc;
    --band-grey: #e4e4e4;
    --ink-dark: #2b2b2b;
    --ink-grey: #5a5a5a;
    --ink-soft: #777777;
    --white: #ffffff;
    --icon-blue: #3a7fc1;
    --label: #333333;
  }
  * { margin: 0; padding: 0; box-sizing: border-box; }
  html, body { width: 1200px; height: 765px; overflow: hidden; }
  body {
    position: relative;
    background: var(--stage);
    font-family: "Open Sans", Arial, sans-serif;
  }
  .card {
    position: absolute;
    top: 302px;
    width: 576px;
    height: 343px;
    border-radius: 34px;
    overflow: hidden;
  }
  .card--front {
    left: 16px;
    background: linear-gradient(160deg, var(--card-light) 0%, var(--card-shade) 100%);
  }
  .card--back { left: 604px; background: var(--orange); }

  /* front */
  .brand-mark {
    position: absolute;
    left: 130px; top: 44px;
    width: 70px; height: 70px;
    border-radius: 50%;
    background: var(--orange);
  }
  .brand-name {
    position: absolute;
    left: 69px; top: 124px;
    font-family: "Orbitron", Arial, sans-serif;
    font-weight: 900;
    font-size: 22px;
    letter-spacing: 1px;
    color: var(--ink-grey);
  }
  .person-name {
    position: absolute;
    left: 260px; top: 168px;
    font-family: "Orbitron", Arial, sans-serif;
    font-weight: 900;
    font-size: 21px;
    letter-spacing: 0.5px;
    color: var(--ink-dark);
  }
  .person-role {
    position: absolute;
    left: 260px; top: 194px;
    font-size: 15px;
    color: var(--orange);
    letter-spacing: -0.3px;
  }
  .person-email {
    position: absolute;
    left: 260px; top: 213px;
    font-size: 13px;
    color: var(--ink-soft);
    letter-spacing: 0.5px;
  }
  .social-list { position: absolute; left: 237px; top: 232px; list-style: none; }
  .social-list li {
    display: flex; align-items: center; gap: 6px;
    height: 21px;
    font-style: italic; font-weight: 600;
    font-size: 16px; color: var(--ink-dark);
    letter-spacing: 0.4px;
  }
  .social-icon { width: 17px; height: 17px; background: var(--icon-blue); border-radius: 2px; }

  /* back */
  .pitch-heading {
    position: absolute;
    left: 69px; top: 38px;
    font-family: "Orbitron", Arial, sans-serif;
    font-weight: 900;
    font-size: 17px;
    letter-spacing: 0.6px;
    color: var(--white);
  }
  .pitch-list { position: absolute; left: 50px; top: 74px; list-style: none; }
  .pitch-list li {
    display: flex; align-items: center; gap: 12px;
    height: 24px;
    font-weight: 600; font-size: 15px; color: var(--white);
  }
  .pitch-bullet { width: 12px; height: 12px; border-radius: 50%; background: var(--white); margin-left: 14px; }
  .pitch-join {
    position: absolute;
    left: 68px; top: 146px;
    font-weight: 600; font-size: 15px; color: var(--white);
  }
  .back-band {
    position: absolute;
    left: 0; top: 174px;
    width: 100%; height: 81px;
    background: var(--band-grey);
  }
  .footer-brand {
    position: absolute;
    left: 48px; top: 275px;
    font-family: "Orbitron", Arial, sans-serif;
    font-weight: 900; font-size: 10px;
    color: var(--white);
  }
  .office-list {
    position: absolute;
    left: 127px; top: 268px;
    list-style: none;
    font-size: 11px; line-height: 14px;
    color: var(--white);
  }

  .face-label {
    position: absolute;
    top: 686px;
    font-family: "Cinzel", Georgia, serif;
    font-size: 14px;
    letter-spacing: 3px;
    color: var(--label);
  }
  .face-label--front { left: 66px; }
  .face-label--back { left: 660px; }
</style>
</head>
<body>

<section class="card card--front" aria-label="Card front">
  <div class="brand-mark"></div>
  <div class="brand-name">PLENVORIA</div>

  <div class="person-name">JONAS REDDICK</div>
  <div class="person-role">Founder and CEO</div>
  <div class="person-email">The@plenvoria.com</div>
  <ul class="social-list">
    <li><span class="social-icon"></span>Chirpline.com/jonasreddick</li>
    <li><span class="social-icon"></span>Friendwall.com/jonasreddick</li>
    <li><span class="social-icon"></span>linkvane.com/in/jonasreddick</li>
  </ul>
</section>

<section class="card card--back" aria-label="Card back">
  <div class="pitch-heading">ARE YOU INTERESTED IN?</div>
  <ul class="pitch-list">
    <li><span class="pitch-bullet"></span>Starting your own Business?</li>
    <li><span class="pitch-bullet"></span>Investing in hot Startups?</li>
    <li><span class="pitch-bullet"></span>Working for the next “Friendwall”?</li>
  </ul>
  <div class="pitch-join">Join us on Friendwall.com/Plenvoria</div>
  <div class="back-band"></div>
  <div class="footer-brand">PLENVORIA</div>
  <ul class="office-list">
    <li>Berlin - Lindenhof 22 | 10117 Berlin | Germany</li>
    <li>Silicon Valley - 812 Orchard Ave | Sunnyvale | CA 94086</li>
  </ul>
</section>

<div class="face-label face-label--front">FRONT</div>
<div class="face-label face-label--back">BACK</div>

</body>
</html>
```